Stationary Design For New Dynamic Company

Hi there we require stationary designed for our new company, we have used "Pixel Harbor" recently for our logo and were very impressed with all of the designers that contributed towards the final result.
What we require now is the following:
Letter head layout (A4)
Business Cards (5 people)
With Compliments slips
Envelopes
Email stationary
We would like to use our current logo design and I have included it for your use (JPEG is the one we have chosen and I have attached an EPS file for your use). Our company specializes in architectural cladding and our products are used by architects, builders and private clients, so we wish for the stationary to be suitable and attractive to our clientele.
I thank everyone in advance for your contributions.
Thank you to all that have provided your designs for this project, I apologize for not providing feedback as I have been away. I have looked at everyone's designs and they all look great and I will come back to those designers that I wish to have changes made sometime today.
Once again a big thank you to all involved.
Business

```html
<!DOCTYPE html>
<html lang="en">
<head>
<meta charset="utf-8">
<title>Facetra Stationery Set</title>
<link href="https://fonts.googleapis.com/css2?family=Dosis:wght@300;400;500;700&display=swap" rel="stylesheet">
<style>
  :root{
    --navy:#123b69;
    --orange:#f7941d;
    --paper:#ffffff;
    --mist:#eef0f3;
    --window:#d3d4d7;
    --ink:#1d3f6b;
    --bg-center:#0b7099;
    --bg-edge:#033a55;
  }
  *{box-sizing:border-box;margin:0;padding:0}
  html,body{width:1200px;height:900px;overflow:hidden}
  body{
    position:relative;
    font-family:"Dosis",sans-serif;
    color:var(--ink);
    background:radial-gradient(ellipse at 45% 45%,var(--bg-center) 0%,#07557a 45%,var(--bg-edge) 100%);
  }
  .piece{position:absolute;background:var(--paper);box-shadow:2px 3px 6px rgba(0,0,0,.35);overflow:hidden;z-index:2}

  .stub,.bar{position:absolute;background:var(--navy)}
  .stub::after,.bar::after{content:"";position:absolute;left:0;right:0;height:2px;background:var(--orange)}
  .brand{position:absolute;display:flex;align-items:center;gap:5px;font-weight:700;color:var(--navy);letter-spacing:.2px;line-height:1}
  .brand .dot{background:var(--orange);display:inline-block}
  .address{position:absolute;font-size:8px;line-height:11px;color:var(--ink)}
  .address b{font-weight:500}
  .footline{position:absolute;left:0;right:0;height:2px;background:linear-gradient(90deg,var(--orange) 0 50%,var(--navy) 50% 100%)}
  .footer-contacts{position:absolute;left:0;right:0;text-align:center;font-size:7.5px;color:var(--ink);white-space:nowrap}
  .footer-contacts span{padding:0 9px;border-left:1px solid var(--navy)}
  .footer-contacts span:first-child{border-left:0}

  /* letterhead sits beneath the envelopes, slip and cards */
  .letterhead{left:542px;top:70px;width:537px;height:758px;z-index:1}
  .letterhead .stub{left:0;top:22px;width:36px;height:16px}
  .letterhead .bar{left:222px;right:0;top:22px;height:16px}
  .letterhead .stub::after,.letterhead .bar::after{top:18px}
  .letterhead .brand{left:56px;top:22px;font-size:21px}
  .letterhead .brand .dot{width:13px;height:13px}
  .letterhead .address{left:222px;top:56px}
  .letterhead .footline{top:714px}
  .letterhead .footer-contacts{top:726px}

  /* envelope back */
  .envelope-back{left:18px;top:62px;width:520px;height:250px;transform:rotate(5deg);transform-origin:left top}
  .envelope-back .flap-bar{position:absolute;left:70px;right:0;top:12px;height:24px;background:var(--navy)}
  .envelope-back .flap-line{position:absolute;left:70px;right:0;top:40px;height:5px;background:var(--orange)}
  .envelope-back .flap-edge{position:absolute;left:0;right:0;top:50px;height:1px;background:#d8dbe0}
  .envelope-back .brand{left:42px;top:14px}
  .envelope-back .brand .dot{width:14px;height:14px}

  /* window envelope */
  .envelope-front{left:75px;top:187px;width:495px;height:248px;background:linear-gradient(180deg,var(--mist) 0%,#fff 60%);z-index:3}
  .envelope-front .stub{left:0;top:20px;width:33px;height:13px}
  .envelope-front .stub::after,.envelope-front .bar::after{top:15px}
  .envelope-front .bar{left:170px;right:0;top:20px;height:13px}
  .envelope-front .bar .url{position:absolute;right:8px;top:2px;font-size:7px;color:#8aa0bd;white-space:nowrap}
  .envelope-front .brand{left:52px;top:21px;font-size:16px}
  .envelope-front .brand .dot{width:10px;height:10px}
  .envelope-front .address{left:171px;top:48px;font-size:7.5px;line-height:10px}
  .envelope-front .window{position:absolute;left:32px;top:139px;width:145px;height:53px;background:var(--window);border-radius:8px}
  .envelope-front .footline{top:236px}

  /* compliment slip */
  .slip{left:36px;top:447px;width:536px;height:252px;background:linear-gradient(180deg,var(--mist) 0%,#fff 70%);z-index:3}
  .slip .stub{left:0;top:23px;width:35px;height:13px}
  .slip .bar{left:185px;right:0;top:23px;height:13px}
  .slip .stub::after,.slip .bar::after{top:15px}
  .slip .brand{left:55px;top:24px;font-size:17px}
  .slip .brand .dot{width:10px;height:10px}
  .slip .address{left:185px;top:52px;font-size:7.5px;line-height:10px}
  .slip .greeting{position:absolute;left:367px;top:48px;font-size:21px;font-weight:300;color:var(--navy);line-height:1;white-space:nowrap}
  .slip .greeting b{font-weight:500}
  .slip .greeting small{display:block;font-size:9px;color:var(--orange);font-weight:400;margin-top:2px}
  .slip .footline{top:226px}
  .slip .footer-contacts{top:236px}

  /* business cards */
  .card{width:231px;height:136px;border-radius:8px;z-index:3}
  .card-front{left:942px;top:190px}
  .card-front .stub{left:0;top:17px;width:10px;height:12px}
  .card-front .bar{left:135px;right:0;top:17px;height:12px}
  .card-front .stub::after,.card-front .bar::after{top:14px}
  .card-front .bar .name{position:absolute;left:8px;top:1px;font-size:8.5px;color:#fff;white-space:nowrap}
  .card-front .bar .name small{font-size:5.5px;padding-left:3px;border-left:1px solid #fff;margin-left:3px}
  .card-front .brand{left:20px;top:18px;font-size:12px}
  .card-front .brand .dot{width:8px;height:8px}
  .card-front .address{left:0;width:104px;top:76px;text-align:right;font-size:7.5px;line-height:11px}
  .card-front .divider{position:absolute;left:113px;top:72px;width:1px;height:50px;background:var(--navy)}
  .card-front .contacts{position:absolute;left:122px;top:75px;list-style:none;font-size:7.5px;line-height:11px;white-space:nowrap}
  .badge{display:inline-block;width:8px;height:8px;font-size:5.5px;line-height:8px;text-align:center;color:#fff;background:var(--navy);margin-right:6px;vertical-align:1px;font-weight:700}
  .card-front .baseline{position:absolute;left:0;right:0;top:126px;height:2px;background:linear-gradient(90deg,var(--navy) 0 50%,var(--orange) 50% 100%)}

  .card-back{left:939px;top:342px}
  .card-back .brand{left:60px;top:46px;font-size:16px}
  .card-back .brand .dot{width:10px;height:10px}
  .card-band{position:absolute;left:0;right:0;bottom:0;height:24px;background:var(--navy);color:#fff;font-size:8px;text-align:center;line-height:24px}
  .card-band::before{content:"";position:absolute;left:0;right:0;top:-4px;height:2px;background:var(--orange)}
  .card-orange{left:935px;top:500px;background:var(--orange)}
  .card-orange .brand{left:60px;top:56px;font-size:16px;color:#fff}
  .card-orange .brand .dot{width:10px;height:10px;background:#fff}
  .card-orange .card-band::before{background:#fff}

  /* email signature */
  .email{left:302px;top:723px;width:206px;height:120px}
  .email .panel{position:absolute;left:7px;right:7px;top:10px;height:52px;background:var(--navy)}
  .email .panel::after{content:"";position:absolute;left:0;right:0;bottom:-4px;height:2px;background:var(--orange)}
  .email .brand{left:10px;top:20px;font-size:11px;color:#fff}
  .email .brand .dot{width:7px;height:7px}
  .email .divider{position:absolute;left:97px;top:6px;width:1px;height:40px;background:#fff}
  .email .contacts{position:absolute;left:103px;top:7px;list-style:none;font-size:7px;line-height:11px;color:#fff;white-space:nowrap}
  .email .contacts .badge{background:var(--orange);width:7px;height:7px;line-height:7px;margin-right:5px}
  .email .note{position:absolute;left:7px;top:74px;font-size:4.6px;line-height:6px;color:var(--ink)}
  .email .social{position:absolute;left:7px;top:95px;display:flex;gap:8px}
  .email .social span{width:16px;height:16px;border-radius:3px;background:#5b7fa6}
</style>
</head>
<body>

  <section class="piece letterhead" aria-label="Letterhead">
    <div class="stub"></div>
    <div class="brand"><span class="dot"></span>FACETRA</div>
    <div class="bar"></div>
    <p class="address">PO Box 4410<br>Alder Court Brookhaven Park<br>New York, USA</p>
    <div class="footline"></div>
    <p class="footer-contacts"><span>P : 555-014-2290</span><span>E : m.ellison@facetra.example</span><span>W : www.facetra.example</span></p>
  </section>

  <section class="piece envelope-back" aria-label="Envelope back">
    <div class="brand"><span class="dot"></span></div>
    <div class="flap-bar"></div>
    <div class="flap-line"></div>
    <div class="flap-edge"></div>
  </section>

  <section class="piece envelope-front" aria-label="Window envelope">
    <div class="stub"></div>
    <div class="brand"><span class="dot"></span>FACETRA</div>
    <div class="bar"><span class="url">www.facetra.example</span></div>
    <p class="address"><b>FACETRA</b><br>PO Box 4410<br>Alder Court Brookhaven Park<br>New York, USA</p>
    <div class="window"></div>
    <div class="footline"></div>
  </section>

  <section class="piece slip" aria-label="With compliments slip">
    <div class="stub"></div>
    <div class="brand"><span class="dot"></span>FACETRA</div>
    <div class="bar"></div>
    <p class="address"><b>FACETRA</b><br>PO Box 4410<br>Alder Court Brookhaven Park<br>New York, USA</p>
    <h2 class="greeting"><b>With</b> Compliments<small>www.facetra.example</small></h2>
    <div class="footline"></div>
    <p class="footer-contacts"><span>P : 555-014-2290</span><span>E : m.ellison@facetra.example</span><span>W : www.facetra.example</span></p>
  </section>

  <section class="piece card card-front" aria-label="Business card front">
    <div class="stub"></div>
    <div class="brand"><span class="dot"></span>FACETRA</div>
    <div class="bar"><span class="name">Mara Ellison<small>President</small></span></div>
    <p class="address">PO Box 4410<br>Alder Court Brookhaven Park<br>New York, USA</p>
    <div class="divider"></div>
    <ul class="contacts">
      <li><span class="badge">P</span>555-014-2290</li>
      <li><span class="badge">E</span>m.ellison@facetra.example</li>
      <li><span class="badge">W</span>www.facetra.example</li>
    </ul>
    <div class="baseline"></div>
  </section>

  <section class="piece card card-back" aria-label="Business card back">
    <div class="brand"><span class="dot"></span>FACETRA</div>
    <div class="card-band">www.facetra.example</div>
  </section>

  <section class="piece card card-orange" aria-label="Business card back, orange">
    <div class="brand"><span class="dot"></span>FACETRA</div>
    <div class="card-band">www.facetra.example</div>
  </section>

  <section class="piece email" aria-label="Email signature">
    <div class="panel">
      <div class="brand"><span class="dot"></span>FACETRA</div>
      <div class="divider"></div>
      <ul class="contacts">
        <li><span class="badge">P</span>555-014-2290</li>
        <li><span class="badge">E</span>m.ellison@facetra.example</li>
        <li><span class="badge">W</span>www.facetra.example</li>
      </ul>
    </div>
    <p class="note">This message was sent by Mara Ellison<br>If you would like to know more about me, you can visit my social profiles</p>
    <div class="social" aria-label="Social profile links">
      <span></span><span></span><span></span><span></span><span></span>
    </div>
  </section>

</body>
</html>
```